依頼詳細
アパートのオーナー様が問合せをしたくなるデザインで
シンプルで、誠実感のあるデザイン。
記載項目
カナメリビング株式会社 岐阜県関市桜台3丁目4-27
スミカネットFC岐阜北店、スミカネットFC各務原21号店、スミカネットFC関店経営。
電話番号0575-38-4716
×
東和住まいリンク株式会社
全国で社宅代行を受託
社宅として、一括借上
サイズ
A4
ページ数
片面
希望イメージ
シンプル 複雑
単色 カラフル
暗い 明るい
日常 高級
遊び心 厳粛
未来的 伝統的
女性的 男性的
希望する色
赤系、青系
納品ファイル
補足説明
添付は会社のいままで作成したチラシ
参考にはしなくてもいいです。
会社の情報のみ参考
■ 選んだ理由

シンプルですが、買取・管理の区別がはっきりしていて分かりやすい。
色合いも、きれいです。

■ 提案者全員のお礼・コメント

この度は、お時間を割いて多数の応募ありがとうございます。
皆様のご提案はそれぞれの良さがあり、大変悩みました。
私の分かりにくい説明でも、ここまで仕上げるのは見事です。
また、機会がありましたら是非お願い致します。

```html
<!DOCTYPE html>
<html lang="ja">
<head>
<meta charset="utf-8">
<title>買取または管理 お任せください</title>
<link href="https://fonts.googleapis.com/css2?family=Noto+Sans+JP:wght@400;700;900&display=swap" rel="stylesheet">
<style>
:root{
  --blue:#1e8fe0;
  --blue-dark:#1b4fa0;
  --pink:#f0557a;
  --pink-dark:#d8355f;
  --yellow:#ffe600;
  --red:#e60033;
  --green:#3aa935;
  --ink:#222;
  --white:#fff;
}
*{margin:0;padding:0;box-sizing:border-box}
html,body{width:846px;height:1200px;overflow:hidden;background:var(--white)}
body{font-family:"Noto Sans JP",sans-serif;color:var(--ink)}
.flyer{position:relative;width:846px;height:1200px;overflow:hidden}
.panel{position:absolute;top:0;height:897px;width:423px}
.panel--buy{left:0;background:var(--blue)}
.panel--manage{left:423px;background:var(--pink)}
.abs{position:absolute}
.lead{top:22px;left:0;width:846px;text-align:center;color:var(--yellow);font-weight:900;font-size:34px;letter-spacing:1px}
.headline{top:80px;left:0;width:846px;text-align:center;color:var(--white);font-weight:900;font-size:100px;line-height:1}
.headline span{display:inline-block;vertical-align:middle}
.or-badge{display:inline-flex!important;align-items:center;justify-content:center;width:78px;height:78px;border-radius:50%;background:var(--white);color:var(--ink);font-size:20px;font-weight:700;margin:0 28px}
.headline-2{top:186px;left:0;width:846px;text-align:center;color:var(--white);font-weight:900;font-size:84px;line-height:1.05;letter-spacing:2px}
.pill{top:292px;width:330px;height:40px;border-radius:20px;background:var(--white);text-align:center;font-weight:900;font-size:24px;line-height:40px}
.pill--buy{left:47px;color:var(--blue-dark)}
.pill--manage{left:470px;color:var(--pink-dark)}
.pill--buy::before,.pill--manage::before{content:"";position:absolute;left:50%;bottom:-10px;margin-left:-10px;border:10px solid transparent;border-bottom:0;border-top-color:var(--white)}
.point{left:24px;width:320px;height:96px}
.point-badge{position:absolute;left:0;top:6px;width:86px;height:40px}
.point-title{position:absolute;left:100px;top:0;color:var(--white);font-weight:900;font-size:36px;line-height:1.2;white-space:nowrap}
.point-title--long{font-size:30px;top:4px}
.point-text{position:absolute;left:100px;top:48px;width:220px;color:var(--white);font-size:12px;line-height:1.5}
.subhead{top:340px;left:423px;width:423px;text-align:center;color:var(--white);font-weight:700;font-size:20px}
.plan{left:508px;width:320px;height:90px}
.plan-no{position:absolute;left:0;top:0;width:62px;height:62px;border-radius:50%;background:var(--white);color:var(--pink);font-weight:900;font-size:40px;text-align:center;line-height:62px}
.plan-title{position:absolute;left:84px;top:2px;color:var(--white);font-weight:900;font-size:36px;line-height:1.2;white-space:nowrap}
.plan-tag{position:absolute;left:86px;top:48px;background:var(--white);color:var(--pink-dark);font-size:12px;font-weight:700;padding:1px 8px}
.plan-text{position:absolute;left:86px;color:var(--white);font-size:12px}
.broker{top:662px;left:508px;width:318px}
.broker-title{color:var(--yellow);font-weight:900;font-size:22px;border-bottom:2px solid var(--yellow);padding-bottom:4px;margin-bottom:8px}
.broker-list{list-style:none;color:var(--white);font-size:13px;line-height:1.6}
.broker-list li::before{content:"● ";color:var(--yellow)}
.staff-photo{left:350px;top:560px;width:145px;height:282px;background:linear-gradient(#3a4f78,#1f2d4a)}
.town{left:0;top:842px;width:846px;height:55px;background:linear-gradient(90deg,#bfe0f7,#f9c6d4)}
.company{top:925px;left:32px}
.company-name{display:flex;align-items:center;gap:10px;font-weight:900;font-size:28px;color:var(--ink);white-space:nowrap}
.company-name i{display:block;width:28px;height:28px;border-radius:50%;background:var(--blue)}
.company-addr{margin-top:10px;font-size:15px}
.company-web{margin-top:4px;font-size:15px;color:var(--blue-dark)}
.contact{top:918px;left:420px;width:410px}
.phone{display:flex;align-items:center;gap:10px;color:var(--red);font-weight:900;font-size:52px;line-height:1;white-space:nowrap}
.hours{margin-top:14px;font-size:14px;line-height:1.6}
.footer{top:1140px;left:0;width:846px;height:44px;display:flex}
.footer-fc{flex:1;background:var(--green);color:var(--white);font-size:14px;font-weight:700;line-height:44px;padding-left:20px;white-space:nowrap}
.footer-partner{flex:1;background:var(--blue-dark);color:var(--white);font-size:14px;font-weight:700;line-height:44px;padding-left:20px;white-space:nowrap}
</style>
</head>
<body>
<main class="flyer">
  <div class="panel panel--buy"></div>
  <div class="panel panel--manage"></div>

  <p class="abs lead">アパート・マンションオーナーの皆様へ</p>
  <h1 class="abs headline"><span>買取</span><span class="or-badge">または</span><span>管理</span></h1>
  <p class="abs headline-2">お任せください!</p>

  <div class="abs pill pill--buy">安心の自社買取</div>
  <div class="abs pill pill--manage">独自の管理システム</div>

  <div class="abs staff-photo" role="img" aria-label="スーツ姿の男性スタッフの写真"></div>

  <section class="buy">
    <div class="abs point" style="top:350px">
      <svg class="point-badge" viewBox="0 0 86 40"><path d="M0 0H66L86 20L66 40H0Z" fill="#fff"/><text x="33" y="26" text-anchor="middle" font-size="15" font-weight="900" fill="#1b4fa0" font-family="Noto Sans JP,sans-serif">POINT</text></svg>
      <div class="point-title">秘密厳守</div>
      <p class="point-text">ご相談内容は外部に漏らさず<br>安心してお任せいただけます。</p>
    </div>
    <div class="abs point" style="top:450px">
      <svg class="point-badge" viewBox="0 0 86 40"><path d="M0 0H66L86 20L66 40H0Z" fill="#fff"/><text x="33" y="26" text-anchor="middle" font-size="15" font-weight="900" fill="#1b4fa0" font-family="Noto Sans JP,sans-serif">POINT</text></svg>
      <div class="point-title">適正価格</div>
      <p class="point-text">地域の相場を踏まえて<br>納得の価格をご提示します。</p>
    </div>
    <div class="abs point" style="top:550px">
      <svg class="point-badge" viewBox="0 0 86 40"><path d="M0 0H66L86 20L66 40H0Z" fill="#fff"/><text x="33" y="26" text-anchor="middle" font-size="15" font-weight="900" fill="#1b4fa0" font-family="Noto Sans JP,sans-serif">POINT</text></svg>
      <div class="point-title">実績豊富</div>
      <p class="point-text">地元で多くの取引実績が<br>あります。</p>
    </div>
    <div class="abs point" style="top:650px">
      <svg class="point-badge" viewBox="0 0 86 40"><path d="M0 0H66L86 20L66 40H0Z" fill="#fff"/><text x="33" y="26" text-anchor="middle" font-size="15" font-weight="900" fill="#1b4fa0" font-family="Noto Sans JP,sans-serif">POINT</text></svg>
      <div class="point-title point-title--long">早期契約決済可</div>
      <p class="point-text">最短二週間での契約・決済にも<br>対応いたします。</p>
    </div>
  </section>

  <section class="manage">
    <p class="abs subhead">3タイプの管理システム</p>
    <div class="abs plan" style="top:380px">
      <div class="plan-no">1</div>
      <div class="plan-title">一般管理</div>
      <p class="plan-text" style="top:52px">管理料は家賃の5%</p>
    </div>
    <div class="abs plan" style="top:470px">
      <div class="plan-no">2</div>
      <div class="plan-title">サブリース</div>
      <span class="plan-tag">家賃保証型</span>
      <p class="plan-text" style="top:72px">管理料は家賃の10%</p>
    </div>
    <div class="abs plan" style="top:560px">
      <div class="plan-no">3</div>
      <div class="plan-title">サブリース</div>
      <span class="plan-tag">社宅一括借上型</span>
      <p class="plan-text" style="top:72px">管理料は家賃の8%</p>
    </div>
    <div class="abs broker">
      <p class="broker-title">仲介に自信があります！</p>
      <ul class="broker-list">
        <li>空室の早期解消</li>
        <li>入居者の審査も安心</li>
        <li>広告掲載を幅広く実施</li>
        <li>退去時の対応も一括</li>
      </ul>
    </div>
  </section>

  <div class="abs town" role="img" aria-label="街並みと住宅のイラスト"></div>

  <section class="abs company">
    <p class="company-name"><i></i>カナメリビング株式会社</p>
    <p class="company-addr">〒501-3299 岐阜県関市桜台3丁目4-27</p>
    <p class="company-web">www.kaname-living.jp</p>
  </section>

  <section class="abs contact">
    <p class="phone">
      <svg width="50" height="50" viewBox="0 0 54 54"><circle cx="27" cy="27" r="27" fill="#e60033"/><path d="M19 14c2 0 4 5 4 6s-2 2-2 3c1 3 5 8 9 9 1 0 2-2 3-2s6 2 6 4-3 6-6 6c-10 0-18-10-19-19 0-4 3-7 5-7z" fill="#fff"/></svg>
      0575-38-4716
    </p>
    <p class="hours">■営業時間／10:00〜19:00<br>■年末年始・お盆を除き年中無休</p>
  </section>

  <footer class="abs footer">
    <div class="footer-fc">スミカネットFC岐阜北店・FC各務原21号店・FC関店経営</div>
    <div class="footer-partner">東和住まいリンク株式会社｜全国で社宅代行を受託</div>
  </footer>
</main>
</body>
</html>
```